Veterinary Business cards

Redesign Business Card

Information needed on Card:
Hours: Mon-Fri: 4pm -10PM; Sat- Sun- 10 AM- 5PM
Help@bayfernvet.com
www.bayfernvet.com
555-718-2946
4173 SE 19th Ave. okc, ok 73958
*No appointment necessary*

Optional:
Our tag line is "We're here when you need us" - If it fits on the cards.

```html
<!DOCTYPE html>
<html lang="en">
<head>
<meta charset="utf-8">
<title>Bayfern Vet Care – Business Card</title>
<link rel="stylesheet" href="https://fonts.googleapis.com/css2?family=Marcellus&family=Bebas+Neue&family=Oswald:wght@300&family=Jost:wght@400&display=swap">
<style>
  :root {
    --page: #ffffff;
    --card-grey: #d4d7d8;
    --card-tan: #b29b78;
    --navy: #163a63;
    --ink: #3a3530;
  }
  html, body {
    margin: 0;
    padding: 0;
    width: 1077px;
    height: 1200px;
    overflow: hidden;
    background: var(--page);
  }
  .canvas {
    position: relative;
    width: 1077px;
    height: 1200px;
  }
  .card {
    position: absolute;
    left: 261px;
    width: 565px;
    height: 338px;
    background: var(--card-grey);
    overflow: hidden;
  }
  .card--front { top: 222px; }
  .card--back { top: 645px; }

  .brand {
    position: absolute;
    left: 0;
    right: 0;
    display: flex;
    align-items: center;
    justify-content: center;
    gap: 10px;
  }
  .brand__dot {
    border-radius: 50%;
    background: var(--navy);
  }
  .brand__name {
    font-family: "Marcellus", serif;
    color: var(--navy);
    letter-spacing: 0.04em;
    white-space: nowrap;
  }
  .card--front .brand { top: 148px; }
  .card--front .brand__dot { width: 16px; height: 16px; }
  .card--front .brand__name { font-size: 40px; }

  .back__logo-side {
    position: absolute;
    left: 0;
    top: 0;
    width: 284px;
    height: 100%;
  }
  .back__logo-side .brand { top: 144px; gap: 6px; }
  .back__logo-side .brand__dot { width: 8px; height: 8px; }
  .back__logo-side .brand__name { font-size: 21px; }

  .back__info-side {
    position: absolute;
    left: 284px;
    top: 0;
    width: 281px;
    height: 100%;
    background: var(--card-tan);
  }
  .person {
    position: absolute;
    right: 86px;
    top: 66px;
    text-align: right;
  }
  .person__name {
    font-family: "Bebas Neue", sans-serif;
    font-size: 26px;
    font-weight: 400;
    letter-spacing: 0.12em;
    line-height: 1;
    margin: 0;
  }
  .person__name .first { color: var(--navy); }
  .person__name .last { color: var(--ink); }
  .person__role {
    font-family: "Oswald", sans-serif;
    font-weight: 300;
    font-size: 10px;
    letter-spacing: 0.1em;
    color: var(--ink);
    margin: 0;
    line-height: 1.1;
  }
  .hours,
  .contact {
    position: absolute;
    left: 17px;
    margin: 0;
    padding: 0;
    list-style: none;
    font-family: "Jost", sans-serif;
    font-size: 11px;
    letter-spacing: 0.06em;
    color: var(--ink);
  }
  .hours { top: 142px; }
  .contact { top: 207px; }
  .hours li,
  .contact li { line-height: 19.5px; }
  .note {
    position: absolute;
    left: 0;
    right: 0;
    bottom: 8px;
    text-align: center;
    font-family: "Jost", sans-serif;
    font-size: 9.5px;
    letter-spacing: 0.1em;
    color: var(--ink);
    margin: 0;
  }
</style>
</head>
<body>
<main class="canvas">
  <section class="card card--front" aria-label="Card front">
    <div class="brand">
      <span class="brand__dot"></span>
      <span class="brand__name">BAYFERN VET CARE</span>
    </div>
  </section>

  <section class="card card--back" aria-label="Card back">
    <div class="back__logo-side">
      <div class="brand">
        <span class="brand__dot"></span>
        <span class="brand__name">BAYFERN VET CARE</span>
      </div>
    </div>
    <div class="back__info-side">
      <div class="person">
        <h1 class="person__name"><span class="first">YOUR</span> <span class="last">NAME</span></h1>
        <p class="person__role">DIRECTOR</p>
      </div>
      <ul class="hours">
        <li>Mon–Fri / 4pm – 10pm</li>
        <li>Sat–Sun / 10am – 5pm</li>
      </ul>
      <ul class="contact">
        <li>TEL / 555-718-2946</li>
        <li>Help@bayfernvet.com</li>
        <li>4173 SE 19th Ave. okc, ok 73958</li>
        <li>www.bayfernvet.com</li>
      </ul>
      <p class="note">/ No appointment necessary /</p>
    </div>
  </section>
</main>
</body>
</html>
```